Rework of Honey Labels - Updated for clarity

I am looking for a re-do of our current creamed honey labels.
Creamed honey is a butter-consistency. There are 5 flavors - original, lavender, chocolate, lemon, cinnamon. We want for it to look sophisticated and luxurious. We want the labels to all be cohesive in this group, but to be able to easily tell the difference between the products by color or something quick besides just words to tell the difference in the product. The product will be an off-white/light amber - except for the chocolate which is the color of Cremoso. There are three size containers for each of these honeys. But we can just focus on the single size for this contest.
The honey market in our area is extremely competitive. Right now, I feel our labels look more homemade. I want something that stands out. We charge a premium for our products. We want for our labels to look like we are a superior product. We are getting our product in many local stores and need to differentiate ourselves. I am attaching some of the labels that I think stand out. As for the labels themselves. They can include that whole blurb about us as Brookvale Meadow - or not. It is not truly necessary to have on the labels. But the logo needs to be included.
For all of these, we want something unique and special. Like you are going for an English mid-day tea at an upscale hotel in London with the Queen (well, I guess now the King...but really I think of the Queen).
I am uploading our current labels and then a few labels to take inspiration from.
Updates
I just reworked the description to be more limited in what I was asking for. Looking for a label for creamed honey in one size jar only. Thank you.

```html
<!DOCTYPE html>
<html lang="en">
<head>
<meta charset="utf-8">
<title>Brookvale Meadow Creamed Honey Labels</title>
<link href="https://fonts.googleapis.com/css2?family=Cinzel:wght@500;700&family=Great+Vibes&display=swap" rel="stylesheet">
<style>
  :root {
    --canvas: #efefeb;
    --ink: #050505;
    --gold: #d3a24c;
    --gold-light: #f3d58a;
    --gold-dark: #9c6a22;
    --original-top: #ea4f2a;
    --original-bottom: #ffd417;
    --chocolate-top: #74420f;
    --chocolate-bottom: #3b1208;
    --lemon-top: #0d3d16;
    --lemon-bottom: #4f8b2d;
    --cinnamon-top: #8c1c19;
    --cinnamon-bottom: #d7711f;
    --lavender-top: #5d2180;
    --lavender-bottom: #3a0a4c;
  }
  * { box-sizing: border-box; margin: 0; padding: 0; }
  html, body { width: 1200px; height: 1200px; overflow: hidden; }
  body { background: var(--canvas); }
  .label-row {
    position: absolute; top: 330px; left: 14px;
    display: flex; gap: 8px;
  }
  .label { position: relative; width: 228px; height: 530px; }
  .label--original { --top: var(--original-top); --bottom: var(--original-bottom); }
  .label--chocolate { --top: var(--chocolate-top); --bottom: var(--chocolate-bottom); }
  .label--lemon { --top: var(--lemon-top); --bottom: var(--lemon-bottom); }
  .label--cinnamon { --top: var(--cinnamon-top); --bottom: var(--cinnamon-bottom); }
  .label--lavender { --top: var(--lavender-top); --bottom: var(--lavender-bottom); }

  .label__panel {
    position: absolute; left: 0; right: 0; top: 148px; bottom: 0;
    background: var(--ink); border: 2px solid var(--gold); overflow: hidden;
  }
  .label__band {
    position: absolute; left: 0; right: 0; top: 0; height: 178px;
    background: linear-gradient(180deg, var(--top), var(--bottom));
  }
  .label__wave { position: absolute; left: 0; top: 150px; width: 100%; height: 40px; }
  .label__tab {
    position: absolute; left: 80px; top: 0; width: 68px; height: 190px;
    background: var(--ink); border: 2px solid var(--gold); border-bottom: none; z-index: 2;
  }
  .label__seal {
    position: absolute; left: 64px; top: 176px; width: 100px; height: 100px;
    border-radius: 50%; background: var(--ink); border: 2px solid var(--gold);
    display: flex; align-items: center; justify-content: center; text-align: center;
    z-index: 3;
  }
  .label__brand {
    font-family: "Cinzel", serif; font-weight: 500; font-size: 11px; line-height: 1.2;
    color: var(--gold);
  }
  .label__flavor {
    position: absolute; left: 0; right: 0; top: 340px; text-align: center;
    font-family: "Great Vibes", cursive; font-size: 30px; color: var(--gold-light);
  }
  .label__name {
    position: absolute; left: 0; right: 0; top: 372px; text-align: center;
    font-family: "Cinzel", serif; font-weight: 700; font-size: 42px; letter-spacing: 1px;
    background: linear-gradient(180deg, var(--gold-light), var(--gold) 55%, var(--gold-dark));
    -webkit-background-clip: text; background-clip: text; color: transparent;
  }
  .label__emblem {
    position: absolute; left: 74px; top: 432px; width: 80px; height: 72px;
    border-radius: 8px;
    background: radial-gradient(circle, var(--gold-light) 0%, var(--gold) 45%, rgba(211,162,76,0.15) 75%);
  }
  .label--lemon .label__emblem { background: radial-gradient(circle, #8fd43a 0%, #4e9a1e 45%, rgba(211,162,76,0.25) 75%); }
  .label--lavender .label__emblem { background: radial-gradient(circle, #b48be0 0%, #7a4aa8 45%, rgba(211,162,76,0.2) 75%); }
  .label--original .label__emblem { background: radial-gradient(circle, #ffb21a 0%, #f06a1a 45%, rgba(211,162,76,0.2) 75%); }
  .label__claim {
    position: absolute; left: 0; right: 0; bottom: 14px; text-align: center;
    font-family: "Cinzel", serif; font-weight: 500; font-size: 14px; letter-spacing: 0.5px;
    color: var(--gold-light);
  }
</style>
</head>
<body>
  <main class="label-row">
    <article class="label label--original">
      <div class="label__tab"></div>
      <div class="label__panel">
        <div class="label__band"></div>
        <svg class="label__wave" viewBox="0 0 228 40" preserveAspectRatio="none"><path d="M0 26 Q60 2 114 8 Q170 14 228 30 L228 40 L0 40 Z" fill="#050505"/><path d="M0 26 Q60 2 114 8 Q170 14 228 30" fill="none" stroke="#d3a24c" stroke-width="3"/><path d="M0 20 Q60 -3 114 3 Q170 9 228 24" fill="none" stroke="#f3d58a" stroke-width="1"/></svg>
      </div>
      <div class="label__seal"><span class="label__brand">Brookvale<br>Meadow</span></div>
      <p class="label__flavor">Original</p>
      <h2 class="label__name">HONEY</h2>
      <div class="label__emblem" role="img" aria-label="Gold bee beside honeycomb cells"></div>
      <p class="label__claim">NATURAL PRODUCT</p>
    </article>
    <article class="label label--chocolate">
      <div class="label__tab"></div>
      <div class="label__panel">
        <div class="label__band"></div>
        <svg class="label__wave" viewBox="0 0 228 40" preserveAspectRatio="none"><path d="M0 26 Q60 2 114 8 Q170 14 228 30 L228 40 L0 40 Z" fill="#050505"/><path d="M0 26 Q60 2 114 8 Q170 14 228 30" fill="none" stroke="#d3a24c" stroke-width="3"/><path d="M0 20 Q60 -3 114 3 Q170 9 228 24" fill="none" stroke="#f3d58a" stroke-width="1"/></svg>
      </div>
      <div class="label__seal"><span class="label__brand">Brookvale<br>Meadow</span></div>
      <p class="label__flavor">Chocolate</p>
      <h2 class="label__name">HONEY</h2>
      <div class="label__emblem" role="img" aria-label="Gold cacao pod split open"></div>
      <p class="label__claim">NATURAL PRODUCT</p>
    </article>
    <article class="label label--lemon">
      <div class="label__tab"></div>
      <div class="label__panel">
        <div class="label__band"></div>
        <svg class="label__wave" viewBox="0 0 228 40" preserveAspectRatio="none"><path d="M0 26 Q60 2 114 8 Q170 14 228 30 L228 40 L0 40 Z" fill="#050505"/><path d="M0 26 Q60 2 114 8 Q170 14 228 30" fill="none" stroke="#d3a24c" stroke-width="3"/><path d="M0 20 Q60 -3 114 3 Q170 9 228 24" fill="none" stroke="#f3d58a" stroke-width="1"/></svg>
      </div>
      <div class="label__seal"><span class="label__brand">Brookvale<br>Meadow</span></div>
      <p class="label__flavor">Lemon</p>
      <h2 class="label__name">HONEY</h2>
      <div class="label__emblem" role="img" aria-label="Green citrus slice with gold rim"></div>
      <p class="label__claim">NATURAL PRODUCT</p>
    </article>
    <article class="label label--cinnamon">
      <div class="label__tab"></div>
      <div class="label__panel">
        <div class="label__band"></div>
        <svg class="label__wave" viewBox="0 0 228 40" preserveAspectRatio="none"><path d="M0 26 Q60 2 114 8 Q170 14 228 30 L228 40 L0 40 Z" fill="#050505"/><path d="M0 26 Q60 2 114 8 Q170 14 228 30" fill="none" stroke="#d3a24c" stroke-width="3"/><path d="M0 20 Q60 -3 114 3 Q170 9 228 24" fill="none" stroke="#f3d58a" stroke-width="1"/></svg>
      </div>
      <div class="label__seal"><span class="label__brand">Brookvale<br>Meadow</span></div>
      <p class="label__flavor">Cinnamon</p>
      <h2 class="label__name">HONEY</h2>
      <div class="label__emblem" role="img" aria-label="Gold star anise spice"></div>
      <p class="label__claim">NATURAL PRODUCT</p>
    </article>
    <article class="label label--lavender">
      <div class="label__tab"></div>
      <div class="label__panel">
        <div class="label__band"></div>
        <svg class="label__wave" viewBox="0 0 228 40" preserveAspectRatio="none"><path d="M0 26 Q60 2 114 8 Q170 14 228 30 L228 40 L0 40 Z" fill="#050505"/><path d="M0 26 Q60 2 114 8 Q170 14 228 30" fill="none" stroke="#d3a24c" stroke-width="3"/><path d="M0 20 Q60 -3 114 3 Q170 9 228 24" fill="none" stroke="#f3d58a" stroke-width="1"/></svg>
      </div>
      <div class="label__seal"><span class="label__brand">Brookvale<br>Meadow</span></div>
      <p class="label__flavor">Lavender</p>
      <h2 class="label__name">HONEY</h2>
      <div class="label__emblem" role="img" aria-label="Lavender sprigs forming a wreath"></div>
      <p class="label__claim">NATURAL PRODUCT</p>
    </article>
  </main>
</body>
</html>
```